Business card design for Plumbing and Gas fitting company

We need a business card design for our plumbing and gas fitting company using the company logo and director details. Design should be modern and eye-catching however kept reasonably simple. This design should be targeted at commercial businesses/work so professionalism is key.

Target Market(s)

Commercial/business

Industry/Entity Type

Plumbing

Contact Information for Business Card

Warren Dohey
Director
027 581 9043
warren@vantorplumbingandgas.example
PO Box 7816
Palmerston North 4472

Font styles to use
Sans Serif

Requirements
Must have
• Logo
• Modern
• Kept simple
Nice to have
• Colour scheme based around logo

```html
<!DOCTYPE html>
<html lang="en">
<head>
<meta charset="utf-8">
<title>Vantor Plumbing &amp; Gas – Business Card</title>
<link rel="stylesheet" href="https://fonts.googleapis.com/css2?family=Source+Sans+3:wght@400;600;700&display=swap">
<style>
  :root {
    --bg-top: #5f6370;
    --bg-bottom: #c9ccd3;
    --card-black: #0b0b0b;
    --card-white: #f2f2f2;
    --brand-blue: #1f6fb6;
    --brand-orange: #d9692a;
    --text-light: #f1f1f1;
    --logo-grey: #6d6d6d;
  }
  * { margin: 0; padding: 0; box-sizing: border-box; }
  html, body { width: 1200px; height: 939px; overflow: hidden; }
  body {
    background: linear-gradient(160deg, var(--bg-top) 0%, #9a9ea8 55%, var(--bg-bottom) 100%);
    font-family: "Source Sans 3", Arial, sans-serif;
    position: relative;
  }
  .card {
    position: absolute;
    width: 580px;
    height: 332px;
    border-radius: 3px;
    overflow: hidden;
    box-shadow: 0 14px 30px rgba(0,0,0,0.35);
  }
  /* back of card */
  .card-back {
    left: 40px; top: 90px;
    background: var(--card-black);
    display: flex; align-items: center; justify-content: center; gap: 18px;
  }
  .brand-mark {
    border-radius: 50%;
    background: var(--brand-orange);
    flex-shrink: 0;
  }
  .card-back .brand-mark { width: 46px; height: 46px; }
  .brand-name {
    color: var(--brand-blue);
    font-weight: 700;
    line-height: 1.05;
  }
  .card-back .brand-name { font-size: 40px; }

  /* front of card */
  .card-front { left: 580px; top: 500px; background: var(--card-black); }
  .card-front .divider { position: absolute; inset: 0; }
  .holder { position: absolute; left: 34px; top: 34px; }
  .holder-name { color: var(--brand-blue); font-size: 34px; font-weight: 600; line-height: 1; }
  .holder-role { color: var(--brand-orange); font-size: 19px; margin-top: 6px; }
  .contact-list { position: absolute; left: 34px; bottom: 26px; list-style: none; }
  .contact-item { display: flex; align-items: center; gap: 12px; margin-top: 12px; color: var(--text-light); font-size: 17px; line-height: 1.15; }
  .contact-icon { width: 34px; height: 34px; border-radius: 5px; background: var(--brand-blue); flex-shrink: 0; display: flex; align-items: center; justify-content: center; }
  .front-logo {
    position: absolute; left: 378px; top: 112px; width: 190px;
    display: flex; flex-direction: column; align-items: center; gap: 8px; text-align: center;
  }
  .front-logo .brand-mark { width: 34px; height: 34px; }
  .front-logo .brand-name { font-size: 26px; }
</style>
</head>
<body>

  <section class="card card-back" aria-label="Card back">
    <span class="brand-mark"></span>
    <span class="brand-name">Vantor<br>Plumbing &amp; Gas</span>
  </section>

  <section class="card card-front" aria-label="Card front">
    <svg class="divider" viewBox="0 0 580 332" preserveAspectRatio="none" aria-hidden="true">
      <path d="M330 0 C 262 80, 292 175, 395 232 S 480 300, 488 332 L580 332 L580 0 Z" fill="var(--brand-blue)" transform="translate(-12 0)"/>
      <path d="M330 0 C 262 80, 292 175, 395 232 S 480 300, 488 332 L580 332 L580 0 Z" fill="var(--card-black)" transform="translate(-8 0)"/>
      <path d="M330 0 C 262 80, 292 175, 395 232 S 480 300, 488 332 L580 332 L580 0 Z" fill="var(--brand-orange)" transform="translate(-5 0)"/>
      <path d="M330 0 C 262 80, 292 175, 395 232 S 480 300, 488 332 L580 332 L580 0 Z" fill="var(--card-white)"/>
    </svg>

    <div class="holder">
      <h1 class="holder-name">Warren Dohey</h1>
      <p class="holder-role">Director</p>
    </div>

    <ul class="contact-list">
      <li class="contact-item">
        <span class="contact-icon">
          <svg width="22" height="22" viewBox="0 0 24 24" aria-hidden="true"><path d="M3 9c0-3 4-5 9-5s9 2 9 5v2h-5V9H8v2H3z M6 12h12l2 8H4z" fill="#fff"/><circle cx="12" cy="16" r="2.2" fill="var(--brand-blue)"/></svg>
        </span>
        <span>027 581 9043</span>
      </li>
      <li class="contact-item">
        <span class="contact-icon">
          <svg width="20" height="22" viewBox="0 0 24 24" aria-hidden="true"><path d="M12 2a7 7 0 0 0-7 7c0 5 7 13 7 13s7-8 7-13a7 7 0 0 0-7-7z" fill="#fff"/><circle cx="12" cy="9" r="2.6" fill="var(--brand-blue)"/></svg>
        </span>
        <span>PO Box 7816<br>Palmerston North 4472</span>
      </li>
      <li class="contact-item">
        <span class="contact-icon">
          <svg width="22" height="18" viewBox="0 0 24 18" aria-hidden="true"><rect x="1" y="1" width="22" height="16" rx="1.5" fill="#fff"/><path d="M1.5 2 12 10 22.5 2 M1.5 16 9 9 M22.5 16 15 9" stroke="var(--brand-blue)" stroke-width="1.6" fill="none"/></svg>
        </span>
        <span>warren@vantorplumbingandgas.example</span>
      </li>
    </ul>

    <div class="front-logo">
      <span class="brand-mark"></span>
      <span class="brand-name">Vantor<br>Plumbing &amp; Gas</span>
    </div>
  </section>

</body>
</html>
```